Biz Card for Harrowfield Property Partners - HWPP

Harrowfield Property Partners is a commercial real estate acquisitions firm. We buy commercial property and need to raise capital from investors for each deal we buy. The vibe needs to be: give us your money, we will multiply it.
Our website: www.hrwpp-example.com
Competitors are: https://velmarholdings-example.com/, https://tribanquepartners-example.com/, http://www.ostrellecapital-example.com/
Target Market(s)
High Net Worth Individuals, Bankers, Insurance Companies, Commercial Real Estate Brokers.
Industry/Entity Type
Investment Banking
Contact Information for Business Card
Name, Title, Addess, Cell#, Office#, email, website
Requirements
Must have
- use one of our logos. See website for look and feel: www.hrwpp-example.com
Nice to have
- see website: www.hrwpp-example.com

```html
<!DOCTYPE html>
<html lang="en">
<head>
<meta charset="utf-8">
<title>Harrowfield Property Partners – Business Card</title>
<link href="https://fonts.googleapis.com/css2?family=Barlow:wght@300;400;500;700&display=swap" rel="stylesheet">
<style>
  :root {
    --navy: #06243b;
    --white: #ffffff;
    --backdrop: #c4dbea;
    --rule: #5a5f7a;
  }
  * { box-sizing: border-box; margin: 0; padding: 0; }
  html, body {
    width: 1200px; height: 1200px; overflow: hidden;
    background: var(--backdrop);
    font-family: "Barlow", Arial, sans-serif;
  }
  .card {
    position: absolute; left: 218px; width: 749px; height: 427px; overflow: hidden;
  }
  .card-front { top: 127px; background: var(--navy); }
  .card-back { top: 602px; background: var(--white); color: var(--navy); }

  .brand-dot {
    position: absolute; left: 317px; top: 121px; width: 108px; height: 108px;
    border-radius: 50%; background: var(--white);
  }
  .brand-name {
    position: absolute; left: 0; right: 0; top: 255px; text-align: center;
    color: var(--white); font-weight: 300; font-size: 21px;
    letter-spacing: 5px; text-transform: uppercase;
  }

  .person { position: absolute; left: 74px; top: 88px; }
  .person-name {
    font-weight: 700; font-size: 29px; letter-spacing: -0.5px; line-height: 1;
  }
  .person-title { font-weight: 400; font-size: 25px; margin-top: 6px; }
  .divider {
    position: absolute; left: 73px; top: 185px; width: 318px; height: 1px;
    background: var(--rule);
  }
  .contacts { position: absolute; left: 48px; top: 220px; list-style: none; }
  .contacts li {
    display: flex; align-items: center; height: 33px;
    font-size: 20px; font-weight: 400;
  }
  .contacts svg { width: 20px; height: 20px; margin-right: 9px; flex: none; }
  .decor-disc {
    position: absolute; left: 502px; top: 60px; width: 308px; height: 308px;
    border-radius: 50%; background: var(--navy);
  }
</style>
</head>
<body>
  <section class="card card-front">
    <div class="brand-dot"></div>
    <p class="brand-name">Harrowfield Property Partners</p>
  </section>

  <section class="card card-back">
    <div class="person">
      <h1 class="person-name">EMPLOYEE NAME</h1>
      <p class="person-title">Employee Title</p>
    </div>
    <div class="divider"></div>
    <ul class="contacts">
      <li>
        <svg viewBox="0 0 20 20"><rect x="6" y="3" width="8" height="14" rx="1.5" fill="none" stroke="#06243b" stroke-width="2"/><rect x="9" y="13.5" width="2" height="1.5" fill="#06243b"/></svg>
        1 (555) 214-0397
      </li>
      <li>
        <svg viewBox="0 0 20 20"><path d="M10 2a5 5 0 0 0-5 5c0 4 5 11 5 11s5-7 5-11a5 5 0 0 0-5-5zm0 7a2 2 0 1 1 0-4 2 2 0 0 1 0 4z" fill="#06243b"/></svg>
        48 Linden Avenue, Marlow Falls, IL
      </li>
      <li>
        <svg viewBox="0 0 20 20"><rect x="2.5" y="5" width="15" height="10" fill="none" stroke="#06243b" stroke-width="1.6"/><path d="M2.5 5l7.5 6 7.5-6" fill="none" stroke="#06243b" stroke-width="1.6"/></svg>
        employee.name@hrwpp-example.com
      </li>
      <li>
        <svg viewBox="0 0 20 20"><circle cx="10" cy="10" r="7" fill="#06243b"/><path d="M7 6c2 1 1 3 3 3s1 3 3 3M12 5c-1 1 0 2 1 2" fill="none" stroke="#fff" stroke-width="1.3"/></svg>
        www.hrwpp-example.com
      </li>
    </ul>
    <div class="decor-disc"></div>
  </section>
</body>
</html>
```